new website screendesign for real estate company

We need new website design
The design must fit into the Corporate Identity design of the company.

old page
http://www.wohnarta.at/

we made some layout.png where you can see the components
http://192.0.2.84:8080/Layout.png
+ its attached

dont design exactly like this we just copied different things together. you can design anything new

the layout.png should just show you the direction. and you can see the basic structure of the page

upper left logo upper right login
navigation
banner slider
search filter

carousel with top objects (real estate)

the lower 4 points are predefined search results. for example when "für Anspruchsvolle" is clicked all luxury objects are displayed
when "WG geeignet" is clicked it shows objects for low budget and students.

also find fitting images for all the once used in layout.png are quite bad

here are some of our previous real estate projects

http://198.51.100.23:8082/trolp/
http://www.barnik.at/
http://www.kelfa-immobilien.at/

```html
<!DOCTYPE html>
<html lang="de">
<head>
<meta charset="utf-8">
<title>Helmora – Immobilien</title>
<link rel="stylesheet" href="https://fonts.googleapis.com/css2?family=Montserrat:wght@400;500;600;700&display=swap">
<style>
:root{
  --orange-deep:#f06a2c;
  --orange:#f39a2b;
  --orange-light:#fbd487;
  --band-pale:#fcd392;
  --band-mid:#f8b15a;
  --footer:#f26b38;
  --blue:#1ea2dc;
  --white:#ffffff;
  --ink:#3a2a1c;
  --ink-soft:#5b4634;
  --canvas:#f1f1f1;
}
*{box-sizing:border-box;margin:0;padding:0}
html,body{width:1200px;height:780px;overflow:hidden}
body{font-family:"Montserrat",sans-serif;color:var(--ink);background:var(--canvas);font-size:12px}
.wrap{width:960px;margin:0 auto;position:relative}

/* header */
.site-header{height:64px;background:linear-gradient(180deg,var(--orange-deep) 0%,var(--orange) 55%,var(--orange-light) 100%)}
.site-header .wrap{height:64px;display:flex;align-items:center}
.brand{display:flex;align-items:center;gap:8px;background:var(--white);padding:6px 12px;border-radius:4px}
.brand-dot{width:18px;height:18px;border-radius:50%;background:var(--orange-deep)}
.brand-name{font-weight:700;font-size:16px;color:var(--orange-deep)}
.lang{display:flex;align-items:center;gap:6px;margin-left:14px;color:var(--white);font-size:11px}
.lang-flag{width:16px;height:11px;background:#2c4a8c}
.company{margin-left:auto;text-align:center;color:var(--white)}
.company-name{font-size:15px;font-weight:500}
.contact{display:flex;gap:16px;justify-content:center;margin-top:4px;font-size:11px}
.contact span{display:flex;align-items:center;gap:5px}
.login{margin-left:auto}
.btn-blue{background:var(--blue);color:var(--white);border:0;font:600 11px "Montserrat",sans-serif;padding:5px 14px;border-radius:2px}

/* nav */
.main-nav{height:30px;background:var(--white);border-bottom:1px solid #e6e6e6}
.main-nav ul{list-style:none;display:flex;height:30px;align-items:stretch}
.main-nav li{display:flex;align-items:center;padding:0 16px;font-size:11px;color:var(--ink-soft)}
.main-nav li.active{background:var(--orange-deep);color:var(--white)}

/* hero */
.hero{height:196px;position:relative;background:linear-gradient(180deg,#b7a78f 0%,#e9e2d6 45%,#8a7b68 100%)}
.hero-caption{position:absolute;left:0;top:18px;width:250px;background:rgba(255,255,255,.92);padding:12px 14px;border-radius:2px}
.hero-caption h2{font-size:14px;font-weight:600;margin-bottom:6px}
.hero-caption p{font-size:10px;color:var(--ink-soft);line-height:1.4;margin-bottom:6px}
.hero-caption a{font-size:10px;color:var(--orange-deep);text-decoration:none}

/* search */
.search-filter{height:58px;background:var(--orange-deep)}
.search-filter .wrap{display:flex;align-items:flex-end;gap:22px;height:58px;padding-bottom:10px}
.field label{display:block;color:var(--white);font-size:10px;margin-bottom:3px}
.select{width:150px;height:20px;background:var(--white);display:flex;align-items:center;justify-content:space-between;padding:0 7px;font-size:10px}
.checks{display:flex;flex-direction:column;gap:3px;color:var(--white);font-size:10px}
.checks span{display:flex;align-items:center;gap:4px}
.box{width:10px;height:10px;background:var(--white)}

/* category slider */
.categories{height:160px;background:var(--band-pale);padding-top:10px;overflow:hidden}
.cat-row{display:flex;gap:4px;justify-content:center;position:relative}
.cat{width:250px}
.cat-photo{height:96px}
.cat h3{font-size:11px;font-weight:600;margin-top:5px}
.cat p{font-size:9.5px;color:var(--ink-soft);line-height:1.3;margin-top:2px}
.arrow{position:absolute;top:32px}
.arrow.prev{left:110px}.arrow.next{right:110px}

/* top objects */
.top-objects{height:176px;background:var(--band-mid);padding-top:14px}
.obj-row{display:flex;gap:8px;justify-content:center}
.obj{width:180px}
.obj-photo{height:118px;position:relative}
.price-tag{position:absolute;left:8px;bottom:6px;display:flex;align-items:center;gap:6px;color:var(--white);font-size:12px}
.price-tag b{background:var(--white);color:var(--ink);font-weight:500;padding:2px 5px}
.obj h4{font-size:11px;font-weight:500;margin-top:6px}
.obj p{font-size:10px;color:var(--white)}

/* footer */
.site-footer{height:96px;background:var(--footer);color:var(--white)}
.footer-top{display:flex;align-items:center;gap:10px;padding-top:10px}
.social{display:flex;gap:2px}
.social span{background:var(--white);color:var(--ink);padding:4px 10px;font-size:11px}
.quick{display:flex;margin-left:auto;align-items:center;gap:6px}
.quick-input{width:230px;height:22px;background:var(--white);display:flex;align-items:center;gap:6px;padding:0 6px;color:#888;font-size:10px}
.footer-cols{display:flex;gap:110px;margin-top:8px;font-size:10px;line-height:1.45}
.footer-cols h5{font-size:11px;font-weight:600}
</style>
</head>
<body>

<header class="site-header">
  <div class="wrap">
    <div class="brand"><span class="brand-dot"></span><span class="brand-name">helmora</span></div>
    <div class="lang"><span class="lang-flag"></span>English</div>
    <div class="company">
      <div class="company-name">Dr. Halberg Immobilien GmbH</div>
      <div class="contact">
        <span><svg width="12" height="12" viewBox="0 0 12 12"><circle cx="6" cy="6" r="6" fill="#fff"/><path d="M4 3.5l1 1.5-.6.7a3.5 3.5 0 0 0 1.9 1.9l.7-.6 1.5 1-.6 1C5.8 9 3 6.2 3 4.1z" fill="#f06a2c"/></svg>+43 1 555 01 20</span>
        <span><svg width="14" height="10" viewBox="0 0 14 10"><rect width="14" height="10" fill="#fff"/><path d="M0 0l7 5 7-5" fill="none" stroke="#f06a2c" stroke-width="1.2"/></svg>office@helmora.at</span>
      </div>
    </div>
    <div class="login"><button class="btn-blue">Login</button></div>
  </div>
</header>

<nav class="main-nav">
  <div class="wrap">
    <ul>
      <li>Immobiliensuche</li>
      <li class="active">Suchauftrag</li>
      <li>Vermieter</li>
      <li>Team</li>
      <li>Services</li>
      <li>Signup</li>
    </ul>
  </div>
</nav>

<section class="hero" role="img" aria-label="Foto eines hellen Wohnzimmers mit weißer Sofalandschaft">
  <div class="wrap">
    <div class="hero-caption">
      <h2>27 Lindenweg Terrace</h2>
      <p>Ruhig gelegenes Penthouse mit weitem Blick über die Stadt und großer Terrasse.</p>
      <a href="#">Mehr lesen</a>
    </div>
  </div>
</section>

<section class="search-filter">
  <div class="wrap">
    <div class="field"><label>Bundesland</label><div class="select">Wien<svg width="8" height="5"><path d="M0 0h8L4 5z" fill="#333"/></svg></div></div>
    <div class="field"><label>Bezirk</label><div class="select">Alle<svg width="8" height="5"><path d="M0 0h8L4 5z" fill="#333"/></svg></div></div>
    <div class="field"><label>Kategorie</label><div class="select">Alle<svg width="8" height="5"><path d="M0 0h8L4 5z" fill="#333"/></svg></div></div>
    <div class="checks"><span><i class="box"></i>Miete</span><span><i class="box"></i>Kauf</span></div>
    <button class="btn-blue">Erweiterte Suche</button>
  </div>
</section>

<section class="categories">
  <div class="cat-row">
    <svg class="arrow prev" width="20" height="34" viewBox="0 0 20 34"><path d="M16 3L4 17l12 14" fill="none" stroke="#fff" stroke-width="3"/></svg>
    <div class="cat">
      <div class="cat-photo" role="img" aria-label="Foto einer jungen Frau mit Tasse auf dem Sofa" style="background:linear-gradient(135deg,#d9c2a6,#8a6a4e)"></div>
      <h3>WG geeignet</h3>
      <p>Verwendbar für alle Leute alle Umwelt. Zuverlässiger für das Leben.</p>
    </div>
    <div class="cat">
      <div class="cat-photo" role="img" aria-label="Foto eines beleuchteten Hauses am Abend" style="background:linear-gradient(135deg,#7a5a3a,#c98c4a)"></div>
      <h3>Anlage</h3>
      <p>Vergrössern Projekt für mehr königlichen Lebens.</p>
    </div>
    <div class="cat">
      <div class="cat-photo" role="img" aria-label="Foto eines eleganten Wohnzimmers" style="background:linear-gradient(135deg,#a8764c,#5e3a24)"></div>
      <h3>Anspruchsvolle</h3>
      <p>Mehr zu den extra großen Menge Dinge kompliziert.</p>
    </div>
    <svg class="arrow next" width="20" height="34" viewBox="0 0 20 34"><path d="M4 3l12 14L4 31" fill="none" stroke="#fff" stroke-width="3"/></svg>
  </div>
</section>

<section class="top-objects">
  <div class="obj-row">
    <div class="obj">
      <div class="obj-photo" role="img" aria-label="Foto eines modernen Hauses mit Glasfront" style="background:linear-gradient(160deg,#3e5aa8,#8c8f8f 60%,#4a4a44)"><div class="price-tag">Kaufen <b>394,000€</b></div></div>
      <h4>Haid</h4><p>Für Haus hier.</p>
    </div>
    <div class="obj">
      <div class="obj-photo" role="img" aria-label="Foto einer hellen Terrasse am Wasser" style="background:linear-gradient(160deg,#c9b89c,#8b775e)"><div class="price-tag">Kaufen <b>194,000€</b></div></div>
      <h4>Haid</h4><p>Für Haus hier.</p>
    </div>
    <div class="obj">
      <div class="obj-photo" role="img" aria-label="Foto eines minimalistischen Innenraums" style="background:linear-gradient(160deg,#d8d4cc,#7b7770)"><div class="price-tag">Kaufen <b>104,000€</b></div></div>
      <h4>Haid</h4><p>Für Haus hier.</p>
    </div>
    <div class="obj">
      <div class="obj-photo" role="img" aria-label="Foto eines blauen Einfamilienhauses mit Garage" style="background:linear-gradient(160deg,#7fa6d8,#5a6f90 60%,#9aa0a4)"><div class="price-tag">Kaufen <b>274,000€</b></div></div>
      <h4>Haid</h4><p>Für Haus hier.</p>
    </div>
  </div>
</section>

<footer class="site-footer">
  <div class="wrap">
    <div class="footer-top">
      <div class="social"><span>Gefällt mir</span><span>Teilen</span></div>
      <div class="quick">
        <div class="quick-input"><svg width="12" height="12" viewBox="0 0 12 12"><circle cx="5" cy="5" r="3.6" fill="none" stroke="#555" stroke-width="1.4"/><path d="M7.6 7.6L11 11" stroke="#555" stroke-width="1.6"/></svg>Direktaufruf Objektnummer</div>
        <button class="btn-blue">Aufrufen</button>
      </div>
    </div>
    <div class="footer-cols">
      <div><h5>Immobiliensuche</h5>Suchauftrag<br>Über uns</div>
      <div><h5>Immobilien</h5>Haus Kaufen<br>Haus Mieten</div>
      <div><h5>Kontakt</h5>Behördlich Konzessionierter<br>Immobilienmakler, 1030 Wien, Lindenweg 18</div>
    </div>
  </div>
</footer>

</body>
</html>
```